@all, I've selected the winner: draft #115 by Grovelantern. I has been a close call, there were a few designs that could have won. To make te final decision I have consulted a group of good friend, which could have been future clients. In the end design #115 won because of it's best combination between professionalism and creativity. Nevertheless, thanks to everyone for participating, I am very happy with the final result!
@all, I see the time has finished. I would like all of you who have contributed for their time and effort. I think the final results are amazing! I will choose the winner soon! Thanks, Leopold
@BorenKell, draft #108,
Thanks for your design. I like the header image. I like less the many colours you've used. Try to follow a bit the last feedback I gave on telephone number, use of little puppets with three products, font of titles, footer, etc. Thanks for your efforts!
@grovelantern, drafts #105, #106 and #107,
Thanks for your new designs! I've thought about it for a long time and came to the conclusion that the full width navigation bar is the best. The separators you've added in design #107 I like as well! You can include them in the newest design. The puppets I like the best in design #115. For now focus on the innerpage. Thanks a lot!!
@plotmakerjo, #103, #104 and #111,
Thanks for your new designs. It's amazing how well you quickly you improve with my feedback!
What you could improve:
- Number and email addres below eachoter, the same width and without a box around them.
- the icons used for news and testimonials seem a bit to 'cartoonish', would prefer something more serious/professional.
- make a second footer for the logo and some details about the company (address, chamber of commerce, etc)
Thanks!!
@tallowcraft, drafts #97, #98, #99, #100, #101, #102,
Thanks for your hard work!!! I see your struggle adding color. In terms of color, i like design #98 te best. But overall I still think #88 is the best. Clear for me is that the wide design favors over the smaller design. The difficulty I have with the colors is I think it's an improvement because it communicates a bit of creativity. What I like less it that it brings the rest of the page out of balance. Especially the news and testimonial column and the footer. Do you see my point?
@grovelantern, draft #115 and #116,
Great design, just great!
Little improvements for the inner pages:
-Could you make the header image the full width and make the three products overlap like they do in the home page, but then from right to left? Like a 90 degree turn counter clockwise?
- Could you add some space between the news, events and testimonial blocks in the right column?
Thanks!
@plotmakerjo, draft #95, #96,
Thanks for your designs, they're very nice for a first concept! :-)
Here's some quick feedback (sorry to be very directive, but I've made some decisions that I would like to update you on):
- loose the language flags, site will only be in Dutch
- loose the searchbox, not necessary.
- loose the icon the the phonenumber, make instead only a phone number and email address.
- change the buttons 'learn more' to only text 'read more'.
- Where does the body text come? People, when accessing the home page, will be interested to have a litte body with text to explain the whole concept.
- footer: can you add a small contact form with name, email and text field?
- footer: can you add the sitemap? Use same font as logo for main chapters and normal text font for sub-chapters.
Please post also a design of the inner pages, like for example draft #91.
@Grovelanter, draft #93
THanks for your latest design, very nice!
Could you make me two little changes?
1. The three little puppets: it seems like they're transparent, so the one in front kind of mixes / overlaps with the onces in the back. Can make it visually more obvious that the one in the front is really in the front and the ones in the back are really in the back.
2. can you shorten the navigation bar an put it on the same height as te logo? Just to see what it does?
Thanks for your hard work!
THanks for your fast response! I've rated your newest design one star less than the previous. I think the lighter green makes it less serious and the fading edges of the photo makes it pretty.
@corvanote, draft #86 and #87,
Nice new design, they're much calmer than the ones earlier, gives more focus on the content.
- telephone/email at right place, ok
- colour purple like less, white background ok
- Icons and fonts of news and testimonals could be improved, a bit more classy would be nice.
- Like your bullits! ;-)
@tallowcraft, draft #85,
Thanks for placing the photo of Urbino! :-) Just one thing, could you put the little puppet of the logo right next to the logo instead of on top? I didn't notice it until now, but I would like to keep it as it was. :-)
How are you doing with the inner pages?
@9rHarborworks, drafts #80, #81, #82, #83,
Thanks for your new designs. I came to the conclusion that I like the designs with a neutral background the best. I helps focussing on the content of the page.
Could you focus on the innerpages now, like i wrote on: March 5, 2011 9:25 AM
I would also appreciate another solution for the call us now and email. Somehow I like them best in the top right corner. :)
@grovelantern, draft #79,
Great your back on track of the first design, nice work this one:
Here's some comments to improve:
- call us/email: just number and email address, both same width.
- Selected navigation menu item, please make full height
- please make team: 3 puppets, one green, two grey and smaller. corporate developemnt: 3 puppets, all green, two smaller.
- Please focus also on the inner pages, follow my post: March 5, 2011 9:25 AM
Thanks!!!
@corvanote, draft #75, #76, #77, #78,
Thanks for your designs, your very productive! But as I understood, you have a team to help you! ;-)#75 is the best, it's the most clean design. The colour purple is well thought of, but isn't very appealing.
I like: the top menu bar is not bad! The way you've handled the three products is nice.
Try to refine the design, try to make it simple and classy. Use also the feedback I already gave!
@tallowcraft, draft #71, #72, #73, #74,
It's just great, very nice design! #71 is the best
Could you do me one favour, can you put the photo of Urbino in the header in stead of this one? I know I'll be able to change it later, but just to see.
Please focus on the inner pages like my post: March 5, 2011 9:25 AM
@Fablorium, draft #69 and #70,
I like the last the best. The little blue box and the blue box stand a bit out though, what happens if you change colour?
What happens if you reduce the space between the body and the header?
Start also thinking about the innerpages, would like to see those, according to my post: March 5, 2011 9:25 AM
Thanks, keep on developing!
@marlon4487, draft#66 and #70,
Thanks for your update! I see your working with my feedback, great.
- what about a white background?
- what about less space for the three products and more for the header image?
- keep on refining the news and testimonial boxes.
@quorbitz, draft #63, #64 and #65,
Great design, nice how you've handled the three products! Little things to improve:
- Leave the butterfly from the header, not necessary, I'll use the photo later
- little puppets in three products a little smaller.
- Chapters in footer as my feedback was to tallow craft.
- Now it's time to focus also on the innerpages, like my post @March 5, 2011 9:25 AM.
Thanks, keep up the good work!
@all,
As we're getting close to the end of the contest and as I've asked you before, I also need your design for the inner pages of the website, that is:
1. what will be the general setup for the page, for example what will happen to the header image, the three product, the column for news and testimonials?
2. How will the pages be formatted, give me an example for:
- General text like, Heading 1/tm6, links, etc.
- an image

```html
<!DOCTYPE html>
<html lang="en">
<head>
<meta charset="utf-8">
<title>Verdancy – Home</title>
<link href="https://fonts.googleapis.com/css2?family=Cinzel:wght@400;600;700&family=Arimo:ital,wght@0,400;0,700;1,400&display=swap" rel="stylesheet">
<style>
:root{
  --green-dark:#3a5628;
  --green-nav:#4b6b35;
  --green-active:#6f934b;
  --green-accent:#6c9a2e;
  --green-light:#a9cd5c;
  --footer:#41602d;
  --footer-strip:#344d24;
  --field:#2f4520;
  --text:#666;
  --heading:#5b5b5b;
  --brand:#4a4a4a;
  --white:#fff;
}
*{box-sizing:border-box;margin:0;padding:0}
html,body{width:1200px;height:915px;overflow:hidden;background:var(--white)}
body{font-family:"Arimo",Arial,sans-serif;color:var(--text);position:relative}
.header{position:absolute;left:0;top:0;width:1200px;height:116px}
.brand{position:absolute;left:230px;top:44px;display:flex;align-items:center;gap:10px}
.brand-square{width:14px;height:14px;background:var(--green-accent)}
.brand-name{font-family:"Arimo",Arial,sans-serif;font-weight:700;font-size:34px;line-height:36px;color:var(--brand)}
.tagline{position:absolute;left:232px;top:88px;font-size:11px;color:#777}
.contact-top{position:absolute;right:225px;top:44px;text-align:right;color:var(--green-nav)}
.contact-top .phone{font-size:36px;line-height:36px;letter-spacing:1px}
.contact-top .email{font-size:14px;letter-spacing:2.2px;margin-top:2px}
.nav{position:absolute;left:0;top:116px;width:1200px;height:34px;background:var(--green-nav)}
.nav ul{list-style:none;display:flex;position:absolute;left:230px;width:745px;height:34px;justify-content:space-between}
.nav li{height:34px;line-height:34px;padding:0 16px;font-size:11px;color:var(--white);letter-spacing:.5px;border-right:1px solid rgba(255,255,255,.15)}
.nav li:last-child{border-right:0}
.nav li.active{background:var(--green-active)}
.hero{position:absolute;left:0;top:150px;width:1200px;height:310px;background:linear-gradient(180deg,#9aa398 0%,#7f8a7c 60%,#5c6a56 100%)}
.slider{position:absolute;left:230px;top:168px;width:755px;height:272px;border:6px solid var(--white);background:var(--white);box-shadow:0 2px 10px rgba(0,0,0,.35)}
.slide-photo{position:absolute;left:0;top:0;width:500px;height:260px;background:linear-gradient(180deg,#c9b08a 0%,#b8926a 55%,#7d6a52 100%)}
.slide-caption{position:absolute;left:0;bottom:0;width:500px;height:96px;background:rgba(30,40,20,.55);padding:12px 14px}
.slide-caption h2{font-family:"Cinzel",serif;font-weight:400;font-size:18px;color:var(--green-light);letter-spacing:1px}
.slide-caption p{font-size:11px;line-height:14px;color:var(--white);margin-top:4px;width:430px}
.products{position:absolute;left:500px;top:0;width:243px;height:260px;background:#f4f6f1}
.product{position:relative;height:86.6px;padding:8px 10px 0 66px;border-bottom:1px solid #dde3d5}
.product:last-child{border-bottom:0}
.product.active{background:var(--white)}
.product.active::before{content:"";position:absolute;left:-14px;top:30px;border-right:14px solid var(--white);border-top:14px solid transparent;border-bottom:14px solid transparent}
.product-figure{position:absolute;left:14px;top:12px;width:40px;height:56px;border-radius:20px 20px 6px 6px;background:linear-gradient(180deg,#8cc043,#5e8e26)}
.product h3{font-family:"Cinzel",serif;font-weight:400;font-size:16px;line-height:16px;color:var(--green-accent)}
.product p{font-size:9px;line-height:11px;color:#777;margin-top:4px}
.product .more{font-size:9px;color:var(--green-nav);font-weight:700;margin-top:2px}
.welcome{position:absolute;left:230px;top:492px;width:505px}
.welcome h1{font-family:"Cinzel",serif;font-weight:400;font-size:28px;color:var(--heading);letter-spacing:1px}
.welcome h1 .name{color:var(--green-accent)}
.welcome p{font-size:11px;line-height:15px;margin-top:14px}
.welcome p.lead{font-weight:700;color:#555}
.divider{position:absolute;left:752px;top:470px;width:1px;height:300px;background:#e2e2e2}
.sidebar{position:absolute;left:770px;top:472px;width:205px}
.sidebar h2{font-family:"Cinzel",serif;font-weight:400;font-size:17px;color:var(--heading);letter-spacing:1px;padding-bottom:5px;border-bottom:1px solid #ddd}
.news-item{display:flex;gap:8px;margin-top:10px}
.news-icon{flex:0 0 18px;height:18px}
.news-item p{font-size:10px;line-height:13px;color:#777}
.testimonials{margin-top:44px}
.quote{font-size:10px;line-height:13px;font-style:italic;color:#777;margin-top:10px;position:relative;padding:0 10px}
.quote::before{content:"“";position:absolute;left:0;top:-4px;font-size:18px;color:#999}
.quote::after{content:"”";position:absolute;right:0;bottom:-8px;font-size:18px;color:#999}
.quote-author{font-size:10px;text-align:right;margin-top:8px;color:var(--green-nav)}
.footer{position:absolute;left:0;top:785px;width:1200px;height:130px;background:var(--footer)}
.footer-strip{height:24px;background:var(--footer-strip);position:relative}
.copyright{position:absolute;left:230px;top:6px;font-size:10px;color:#dfe8d3}
.connect{position:absolute;right:225px;top:4px;display:flex;gap:8px;align-items:center;font-size:10px;color:#dfe8d3}
.connect span.square{width:15px;height:15px;border-radius:2px;background:#8fb45a}
.footer-col{position:absolute;top:30px}
.footer-col h4{font-family:"Cinzel",serif;font-weight:400;font-size:14px;line-height:16px;color:var(--white);letter-spacing:1px;margin-bottom:4px}
.footer-col ul{list-style:none}
.footer-col li{font-size:9.5px;line-height:13.5px;color:#d3e0c4}
.contact-form input,.contact-form textarea{display:block;width:185px;height:14px;margin-bottom:3px;background:var(--field);border:1px solid #5b7a45;color:#d3e0c4;font-size:8.5px;line-height:10px;padding:0 5px;font-family:inherit}
.contact-form input::placeholder,.contact-form textarea::placeholder{color:#b9c9a8}
.contact-form textarea{height:26px;resize:none;padding-top:1px}
.contact-form button{display:block;font-size:8.5px;line-height:10px;height:15px;padding:0 8px;border:1px solid #ccc;background:var(--white);color:#333;font-family:inherit}
</style>
</head>
<body>
<header class="header">
  <div class="brand"><span class="brand-square"></span><span class="brand-name">Verdancy</span></div>
  <div class="tagline">Persoonlijke, Team en Organisatieontwikkeling in Italië</div>
  <div class="contact-top">
    <div class="phone">097-555-0142</div>
    <div class="email">INFO@VERDANCY.COM</div>
  </div>
</header>

<nav class="nav">
  <ul>
    <li class="active">HOME</li><li>ABOUT</li><li>PROGRAMS</li><li>BENEFITS</li><li>ACCOMMODATION</li><li>LOCATION</li><li>NEWS</li><li>CONTACTS</li>
  </ul>
</nav>

<section class="hero" role="img" aria-label="Photograph of a historic Italian hill town with towers and rooftops"></section>
<div class="slider">
  <div class="slide-photo" role="img" aria-label="Photograph of a renaissance palace facade on a town square"></div>
  <div class="slide-caption">
    <h2>TEAM DEVELOPMENT</h2>
    <p>Shared learning in an inspiring setting. Teams build trust, open communication and leadership during a stay in the historic heart of an Italian town, away from daily routine and deadlines.</p>
  </div>
  <div class="products">
    <div class="product">
      <div class="product-figure" role="img" aria-label="Illustrated single figure for personal development"></div>
      <h3>PERSONAL<br>DEVELOPMENT</h3>
      <p>Reflect, grow and find new focus in a calm setting.</p>
      <div class="more">more »</div>
    </div>
    <div class="product active">
      <div class="product-figure" role="img" aria-label="Illustrated group of figures for team development"></div>
      <h3>TEAM<br>DEVELOPMENT</h3>
      <p>Work together on trust, roles and shared goals.</p>
      <div class="more">more »</div>
    </div>
    <div class="product">
      <div class="product-figure" role="img" aria-label="Illustrated group of figures for corporate development"></div>
      <h3>CORPORATE<br>DEVELOPMENT</h3>
      <p>Tailored programmes that move whole organisations forward.</p>
      <div class="more">more »</div>
    </div>
  </div>
</div>

<main class="welcome">
  <h1>WELCOME TO <span class="name">VERDANCY</span></h1>
  <p>Our programmes combine personal, team and corporate development with a stay in a quiet Italian town. Guided sessions, walks and shared meals give room to step back from daily work. Participants gain clear insight into their own strengths, learn to cooperate with more ease and return home with concrete steps to put into practice. Every programme is shaped around the goals of the group and led by experienced coaches.</p>
  <p class="lead">Each stay includes comfortable accommodation, local meals and time to explore the surrounding hills, so that learning and rest go hand in hand from the first day to the last.</p>
</main>

<div class="divider"></div>

<aside class="sidebar">
  <h2>LATEST NEWS</h2>
  <div class="news-item">
    <svg class="news-icon" viewBox="0 0 18 18"><rect x="2" y="1" width="14" height="16" fill="#eee" stroke="#aaa"/><path d="M5 6h8M5 9h8M5 12h6" stroke="#999"/></svg>
    <p>New spring programme for small teams now open for booking</p>
  </div>
  <div class="news-item">
    <svg class="news-icon" viewBox="0 0 18 18"><rect x="2" y="1" width="14" height="16" fill="#eee" stroke="#aaa"/><path d="M5 6h8M5 9h8M5 12h6" stroke="#999"/></svg>
    <p>Coaching week in autumn adds extra walking sessions</p>
  </div>
  <div class="testimonials">
    <h2>TESTIMONIALS</h2>
    <p class="quote">A week that changed how our team works together. Clear sessions, warm hosts and a setting that invites real reflection.</p>
    <p class="quote-author">— Marieke de Vries, Utrecht</p>
  </div>
</aside>

<footer class="footer">
  <div class="footer-strip">
    <div class="copyright">Copyright © 2011 Verdancy. All Rights Reserved.</div>
    <div class="connect">connect with us: <span class="square"></span><span class="square"></span><span class="square"></span><span class="square"></span></div>
  </div>
  <div class="footer-col" style="left:245px">
    <h4>QUICKLINKS</h4>
    <ul><li>Home</li><li>About</li><li>Programs</li><li>Benefits</li><li>News</li></ul>
  </div>
  <div class="footer-col" style="left:405px">
    <h4>SERVICES</h4>
    <ul><li>Accommodation</li><li>Location</li><li>Personal Development</li><li>Team Development</li><li>Corporate Development</li></ul>
  </div>
  <div class="footer-col" style="left:600px">
    <h4>OTHER LINKS</h4>
    <ul><li>Contact</li><li>Sitemap</li><li>Term Of Use</li><li>Privacy Statement</li><li>Impressum</li></ul>
  </div>
  <div class="footer-col contact-form" style="left:785px">
    <h4>GET IN TOUCH:</h4>
    <input type="text" placeholder="Your Name">
    <input type="text" placeholder="Your Email">
    <textarea placeholder="Your Message"></textarea>
    <button type="button">Submit</button>
  </div>
</footer>
</body>
</html>
```